Digital Marketing Website Design

I need the homepage designed for my new digital marketing agency I am starting. The main goal for this homepage is to drive people to make an appointment for me to discuss their upcoming projects. Here are some examples of the layouts that I would like to emulate.
https://www.tallmarsh.com/
https://www.quillforge.com/
https://pebblenook.com/
https://drvenholt.com/
https://www.quietlyrooted.org/
My main focus is to attract leads that need help with running digital ads such as Chatterly ads and Finder Promos. I do offer other services like SEO and other things but the main focus is digital Ads.
The final design should communicate Orchid Digital is a Digital marketing strategist building predictable revenue for small businesses through digital ads, email and marketing automation.
Target Market(s)
30-55, business owners, income 100K+, ecommerce companies, etc.
Industry/Entity Type
Digital Marketing
Number of Pages Required
2 page
Font styles to use
Requirements
Must have
- An appealing look and feel set to drive people to make an appointment.
Logo
There needs to be a call to action button in the far right of the navigation
The same call to action in the navigation needs to be in each section on the homepage.
I need the homepage and an about us page.

```html
<!DOCTYPE html>
<html lang="en">
<head>
<meta charset="utf-8">
<title>Orchid Digital — Mobile Menu</title>
<link rel="stylesheet" href="https://fonts.googleapis.com/css2?family=Raleway:wght@400;500;600;700&display=swap">
<style>
  :root {
    --white: #ffffff;
    --purple-deep: #7b55e0;
    --purple-mid: #9a5fe2;
    --purple-light: #b77fe6;
    --lavender: #c9a8f0;
    --icon-purple: #8d5fe6;
    --ink: #222222;
    --nav-text: #4a4a4a;
    --cta-text: #5b6b7c;
    --divider: #ececec;
    --logo-red: #e2492a;
  }
  * { box-sizing: border-box; margin: 0; padding: 0; }
  html, body {
    width: 1023px;
    height: 1200px;
    overflow: hidden;
    font-family: "Raleway", sans-serif;
    background: var(--white);
  }
  .page {
    position: relative;
    width: 1023px;
    height: 1200px;
    overflow: hidden;
  }
  .hero-backdrop {
    position: absolute;
    left: 0; top: 156px;
    width: 1023px; height: 1044px;
    background:
      radial-gradient(ellipse 60% 40% at 50% 62%, rgba(120, 90, 220, 0.55), transparent 70%),
      linear-gradient(90deg, var(--purple-light) 0%, var(--purple-mid) 45%, var(--purple-deep) 100%);
  }
  .hero-backdrop::after {
    content: "";
    position: absolute;
    left: 0; right: 0; bottom: 0; height: 380px;
    background: linear-gradient(180deg, rgba(201, 168, 240, 0) 0%, var(--lavender) 100%);
  }
  .site-header {
    position: absolute;
    left: 0; top: 0;
    width: 1023px; height: 156px;
    background: var(--white);
    display: flex;
    align-items: center;
    justify-content: space-between;
    padding: 0 88px 0 87px;
    border-bottom: 1px solid var(--divider);
    z-index: 3;
  }
  .brand {
    display: flex;
    align-items: center;
    gap: 14px;
    font-weight: 700;
    font-size: 38px;
    letter-spacing: 1px;
    color: var(--ink);
  }
  .brand-dot {
    width: 26px; height: 26px;
    border-radius: 50%;
    background: var(--logo-red);
  }
  .menu-close { width: 48px; height: 48px; display: block; }
  .mobile-menu {
    position: absolute;
    left: 30px; top: 156px;
    width: 964px; height: 401px;
    background: var(--white);
    border-radius: 0 0 46px 46px;
    list-style: none;
    z-index: 2;
  }
  .mobile-menu li {
    height: 99px;
    display: flex;
    align-items: center;
    justify-content: center;
    border-bottom: 2px solid var(--divider);
    font-size: 25px;
    font-weight: 500;
    letter-spacing: 2.5px;
    color: var(--nav-text);
  }
  .mobile-menu li:last-child { border-bottom: none; height: 104px; }
  .mobile-menu .menu-cta { color: var(--cta-text); font-weight: 600; letter-spacing: 2px; }
  .hero-offer {
    position: absolute;
    left: 0; top: 582px;
    width: 1023px;
    text-align: center;
    color: var(--white);
    font-size: 34px;
    font-weight: 500;
    z-index: 1;
  }
  .cta-button {
    position: absolute;
    left: 186px; top: 667px;
    width: 651px; height: 85px;
    border-radius: 43px;
    background: var(--white);
    color: var(--ink);
    font-size: 34px;
    font-weight: 500;
    display: flex;
    align-items: center;
    justify-content: center;
    z-index: 1;
  }
  .feature-card {
    position: absolute;
    left: 30px; top: 828px;
    width: 964px; height: 420px;
    background: var(--white);
    border-radius: 46px;
    z-index: 1;
  }
  .feature-icon {
    position: absolute;
    left: 394px; top: 59px;
    width: 176px; height: 176px;
    border-radius: 50%;
    background: var(--icon-purple);
  }
  .feature-title {
    position: absolute;
    left: 0; top: 287px;
    width: 964px;
    text-align: center;
    font-size: 37px;
    font-weight: 500;
    letter-spacing: 3px;
    color: var(--ink);
  }
</style>
</head>
<body>
<div class="page">
  <div class="hero-backdrop" role="img" aria-label="Laptop on a desk under a purple gradient overlay"></div>

  <header class="site-header">
    <div class="brand"><span class="brand-dot"></span>Orchid Digital</div>
    <svg class="menu-close" viewBox="0 0 48 48" aria-label="Close menu">
      <line x1="4" y1="4" x2="44" y2="44" stroke="#6b7a88" stroke-width="4"/>
      <line x1="44" y1="4" x2="4" y2="44" stroke="#6b7a88" stroke-width="4"/>
    </svg>
  </header>

  <ul class="mobile-menu">
    <li>NAV1</li>
    <li>NAV2</li>
    <li>NAV3</li>
    <li class="menu-cta">Schedule an Appointment</li>
  </ul>

  <p class="hero-offer">Free Chatterly Ads Checklist</p>
  <div class="cta-button">Schedule an Appointment</div>

  <section class="feature-card">
    <div class="feature-icon" role="img" aria-label="Icon of a team meeting around a table"></div>
    <h2 class="feature-title">We are the best</h2>
  </section>
</div>
</body>
</html>
```